International Travel & Visas Firm needs a Schengen Visa eBook Cover Design

We need an ebook cover design for an online based travel, immigration, visas & nationality law firm called 'OrB' (orbit and borderway). We are all about helping people overcome the obstacles to travel and ensuring that people achieve their dreams and ambitions through travel to various destinations and bettering their lives.This initial ebook cover is for our downloaded pdf ebook all about Schengen visas and travelling to any of the 26 European countries that form the Schengen Zone.We want people to be excited about buying this book even before receiving it.We would like to see amazing designs that also speak to our logo and new branding.Check out https://orbitandborderway.example/schengen-visas/ and http://orbitandborderway.pages.funnelvex.example/start-your-schengen-visa-application

Target Market(s)

Travellers that want to get a visa to travel around Europe

Industry/Entity Type

Travel Industry

Colors
fbee3d
faa54b

Requirements
Must have
• - Title:
• Passport Path Primer
Nice to have
• - tagline:
• Unshackle your feet and roam 26 European Countries
• - OrB Logo
• - Reference to it being an insider's guide to Schengen Visas
• - a play on the word OrB (I am)

```html
<!DOCTYPE html>
<html lang="en">
<head>
<meta charset="utf-8">
<title>Passport Path Primer — OrB</title>
<link rel="stylesheet" href="https://fonts.googleapis.com/css2?family=Bebas+Neue&family=Open+Sans:ital,wght@0,400;0,700;1,300;1,400&display=swap">
<style>
  :root {
    --page: #f2f2f2;
    --ocean: #0a5f96;
    --land: #e2e3e4;
    --paper: #ffffff;
    --ink: #45474a;
    --orange: #f48634;
    --gold: #f6ea3c;
  }
  * { box-sizing: border-box; margin: 0; padding: 0; }
  html, body { width: 1008px; height: 1200px; overflow: hidden; background: var(--page); }
  .cover {
    position: absolute; left: 105px; top: 0;
    width: 798px; height: 1200px;
    background: var(--ocean); overflow: hidden;
    font-family: "Open Sans", sans-serif;
  }
  .cover-art { position: absolute; inset: 0; width: 798px; height: 1200px; }
  .brand {
    position: absolute; right: 69px; top: 58px; text-align: right;
    color: var(--ink);
  }
  .brand-name { font-weight: 700; font-size: 50px; line-height: 1; letter-spacing: 1px; }
  .brand-caption { font-weight: 700; font-size: 9px; margin-top: 12px; letter-spacing: 0.2px; }
  .title {
    position: absolute; right: 68px; top: 528px; text-align: right;
    font-family: "Bebas Neue", sans-serif; font-weight: 400;
    font-size: 156px; line-height: 0.76; letter-spacing: 1px;
  }
  .title-line { display: block; }
  .title-line--lead { color: var(--ink); }
  .title-line--accent { color: var(--orange); margin-top: 5px; font-size: 146px; }
  .subtitle {
    position: absolute; right: 70px; top: 808px; text-align: right;
    font-style: italic; font-weight: 400; font-size: 31px; line-height: 44px;
  }
  .subtitle-lead { color: var(--ink); display: block; }
  .subtitle-accent { color: var(--orange); display: block; }
  .tagline {
    position: absolute; left: 0; right: 0; top: 1088px; text-align: center;
    color: var(--paper);
  }
  .tagline-lead { display: block; font-size: 23px; line-height: 30px; padding-left: 20px; }
  .tagline-focus { display: block; color: var(--gold); font-size: 58px; line-height: 66px; letter-spacing: -0.5px; padding-left: 60px; }
</style>
</head>
<body>
  <main class="cover">
    <svg class="cover-art" viewBox="0 0 798 1200" aria-hidden="false">
      <path class="map-region" role="img" aria-label="Map of Europe in pale grey"
            fill="var(--land)"
            d="M266,0 H798 V265 C740,280 700,250 640,265 C590,280 560,300 520,300 C470,305 420,300 380,315 C340,320 315,290 318,250 C322,200 340,170 330,130 C315,90 285,50 266,0 Z"/>
      <circle class="star-ring" role="img" aria-label="Ring of twelve gold stars"
              cx="135" cy="148" r="95" fill="none" stroke="var(--gold)" stroke-width="16" opacity="0.35"/>
      <path class="traveller-band" role="img" aria-label="Silhouettes of travellers walking around the edge of the continent"
            fill="var(--paper)" opacity="0.35"
            d="M210,340 C260,330 290,320 310,330 C230,420 180,520 162,674 C165,780 215,880 240,1010 C200,1000 150,940 120,860 C85,760 80,640 110,540 C140,450 175,380 210,340 Z
               M520,290 C560,280 620,300 660,330 C700,340 760,330 798,320 V420 C740,400 690,390 620,360 C590,330 560,300 520,290 Z"/>
      <path class="headline-field" fill="var(--paper)"
            d="M307,349 C380,330 450,330 500,320 C545,310 575,300 610,312 C640,325 650,360 690,380 C730,400 770,410 798,415 V1093 C650,1070 480,1030 374,973 C260,910 190,810 162,674 C155,560 200,460 240,420 C265,390 285,365 307,349 Z"/>
    </svg>

    <div class="brand">
      <div class="brand-name">OrB</div>
      <div class="brand-caption">orbit and borderway</div>
    </div>

    <h1 class="title">
      <span class="title-line title-line--lead">Passport</span>
      <span class="title-line title-line--accent">Path Primer</span>
    </h1>

    <p class="subtitle">
      <span class="subtitle-lead">Insider's guide to</span>
      <span class="subtitle-accent">Schengen Visas</span>
    </p>

    <p class="tagline">
      <span class="tagline-lead">Unshackle your feet and roam</span>
      <span class="tagline-focus">26 EUROPEAN COUNTRIES</span>
    </p>
  </main>
</body>
</html>
```